Online Art Gallery & Art Management Firm looking for a business card

I'm launching an online art gallery (paintings, photography, drawings, furniture, books, ...) where people can buy all types of art. It's a platform where young and unknown artists can showcase their oeuvre.

Additionally, the venture will act as my advising company for artists. I help them out with their business side of life and become their representative.

The company name: The Velvet Parlour
Logo is attached

I'm looking for something very classy and upmarket.
Updates

Reason: Logo wasn't finished yet...

The design should include the following information: - Name: Pieter Vandomme - Title: Founder - Mobile: +32 (0) 486 514 362 - E-mail: pieter@velvet-parlour.example - Website www.velvet-parlour.example I prefer the have the logo (without website) on the one side and the information on the other. Best regards Pieter

Target Market(s)

Art buyers / art dealers / artists / middle class / upmarket /

Industry/Entity Type

Artists

Colors

Designer to choose colors to be used in the design.

Requirements
Must have
• Must communicate credibility, trust and integrity
Nice to have
• Something classy, chique
Should not have
• Nothing to artistic or creative

```html
<!DOCTYPE html>
<html lang="en">
<head>
<meta charset="utf-8">
<title>The Velvet Parlour — Business Card</title>
<link rel="stylesheet" href="https://fonts.googleapis.com/css2?family=Josefin+Sans:wght@300;400&display=swap">
<style>
  :root {
    --canvas: #e6e3df;
    --card-dark: #0f1917;
    --card-dark-edge: #16221f;
    --card-light: #fbfbfa;
    --ink-light: #f2f2f0;
    --ink-dark: #1b1b1b;
    --ink-muted: #3a3a3a;
    --shadow: rgba(0, 0, 0, 0.16);
  }
  * { box-sizing: border-box; margin: 0; padding: 0; }
  html, body {
    width: 1200px;
    height: 800px;
    overflow: hidden;
    background: var(--canvas);
    font-family: "Josefin Sans", "Helvetica Neue", Arial, sans-serif;
  }
  .sheet {
    position: relative;
    width: 1200px;
    height: 800px;
    display: flex;
    align-items: center;
    justify-content: center;
    gap: 40px;
  }
  .card {
    position: relative;
    width: 530px;
    height: 343px;
    box-shadow: 0 10px 28px var(--shadow);
  }
  /* Logo side */
  .card--back {
    background: linear-gradient(135deg, var(--card-dark-edge) 0%, var(--card-dark) 55%);
    display: flex;
    align-items: center;
    justify-content: center;
  }
  .brand-name {
    color: var(--ink-light);
    font-weight: 300;
    font-size: 30px;
    letter-spacing: 0.22em;
    text-transform: uppercase;
    padding-left: 0.22em;
  }
  /* Information side */
  .card--front {
    background: var(--card-light);
  }
  .holder {
    position: absolute;
    left: 92px;
    top: 110px;
  }
  .holder-name {
    color: var(--ink-dark);
    font-weight: 300;
    font-size: 25px;
    letter-spacing: 0.3em;
    text-transform: uppercase;
    white-space: nowrap;
  }
  .holder-title {
    margin-top: 8px;
    padding-left: 118px;
    color: var(--ink-muted);
    font-weight: 300;
    font-size: 12px;
    letter-spacing: 0.42em;
    text-transform: uppercase;
  }
  .contact {
    position: absolute;
    left: 34px;
    right: 34px;
    bottom: 44px;
    color: var(--ink-dark);
    font-weight: 400;
    font-size: 10.5px;
    letter-spacing: 0.02em;
    white-space: nowrap;
  }
  .contact .sep { margin: 0 6px; }
</style>
</head>
<body>
  <main class="sheet">
    <section class="card card--back" aria-label="Logo side">
      <p class="brand-name">The Velvet Parlour</p>
    </section>

    <section class="card card--front" aria-label="Information side">
      <div class="holder">
        <h1 class="holder-name">Pieter Vandomme</h1>
        <p class="holder-title">Founder</p>
      </div>
      <p class="contact">
        <span class="contact-phone">+32 (0) 486 514 362</span><span class="sep">|</span><span class="contact-email">pieter@velvet-parlour.example</span><span class="sep">|</span><span class="contact-web">www.velvet-parlour.example</span>
      </p>
    </section>
  </main>
</body>
</html>
```